Financial Planning business needs a new Business Card design

We need a business card design for an Australian financial planning business. I am looking for a clean simple design

Target Market(s)

People aged 25-40

Industry/Entity Type

Financial Service

Contact Information for Business Card

On the front of the card we need the following information:
Name: Colin Merrow (First Name Green: #006838 and last name Grey: #414042)
Position: Financial Adviser
Qualifications: BEc(Hons), AdDipFS(FP), Dip FMBM, CFL®
Mobile: 0437 512 604
Email: colin@brightledgeplan.com.au

On the back of the card we need:
Postal address: PO BOX 5307, PERTH BC, WA 6849
Website: www.brightledgeplan.com.au
Text: AFS Licence No. 518760

The fields need to be able to be edited.

Font styles to use
Sans Serif

Requirements
Must have
• Information listed above

```html
<!DOCTYPE html>
<html lang="en">
<head>
<meta charset="utf-8">
<title>Brightledge – Business Card</title>
<link rel="stylesheet" href="https://fonts.googleapis.com/css2?family=Open+Sans:wght@400;600;700&display=swap">
<style>
  :root {
    --brand-green: #006838;
    --brand-grey: #414042;
    --card-white: #ffffff;
    --stage: #ebe8e4;
    --text-dark: #333335;
    --rule: #414042;
  }
  * { margin: 0; padding: 0; box-sizing: border-box; }
  html, body { width: 1200px; height: 1000px; overflow: hidden; }
  body {
    background: var(--stage);
    font-family: "Open Sans", Arial, sans-serif;
    position: relative;
  }
  .card {
    position: absolute;
    left: 265px;
    width: 666px;
    height: 397px;
    box-shadow: 0 3px 10px rgba(0,0,0,0.18);
  }
  .card--front { top: 73px; background: var(--card-white); }
  .card--back { top: 532px; background: var(--brand-green); }

  .accent-bar {
    position: absolute;
    left: 0; top: 75px;
    width: 10px; height: 57px;
    background: var(--brand-green);
  }
  .wordmark {
    position: absolute;
    font-weight: 700;
    font-size: 39px;
    letter-spacing: 0;
    line-height: 1;
    white-space: nowrap;
  }
  .card--front .wordmark { left: 33px; top: 85px; color: var(--brand-grey); }
  .card--back .wordmark { left: 46px; top: 180px; color: var(--card-white); }

  .contact {
    position: absolute;
    left: 371px; top: 224px;
    padding-left: 27px;
    border-left: 2px solid var(--rule);
    height: 140px;
    color: var(--text-dark);
  }
  .contact__name {
    font-size: 22px;
    font-weight: 600;
    line-height: 1;
    margin-top: -1px;
    text-transform: uppercase;
    color: var(--brand-grey);
  }
  .contact__first { color: var(--brand-green); }
  .contact__role { font-size: 15px; line-height: 20px; margin-top: 2px; }
  .contact__quals { font-size: 15px; line-height: 20px; margin-top: 5px; }
  .contact__lines { list-style: none; margin-top: 9px; font-size: 15.5px; line-height: 24px; }
  .contact__lines li { display: flex; align-items: center; gap: 8px; }
  .contact__lines svg { width: 15px; height: 13px; fill: var(--brand-green); }

  .company-info {
    position: absolute;
    left: 355px; top: 168px;
    padding-left: 13px;
    border-left: 2px solid var(--card-white);
    color: var(--card-white);
    font-size: 15.5px;
    line-height: 21.5px;
  }
</style>
</head>
<body>
  <section class="card card--front" aria-label="Business card front">
    <div class="accent-bar"></div>
    <div class="wordmark">BRIGHTLEDGE</div>
    <div class="contact">
      <p class="contact__name"><span class="contact__first">Colin</span> Merrow</p>
      <p class="contact__role">Financial Adviser</p>
      <p class="contact__quals">BEc(Hons), AdDipFS(FP),<br>Dip FMBM, CFL®</p>
      <ul class="contact__lines">
        <li>
          <svg viewBox="0 0 15 13" aria-hidden="true"><path d="M1 4c0-2 3-3 6.5-3S14 2 14 4v1h-3V3.6H4V5H1z"/><path d="M3 6h9l1.5 6h-12z"/></svg>
          <span>0437 512 604</span>
        </li>
        <li>
          <svg viewBox="0 0 15 13" aria-hidden="true"><path d="M0 2h15v1L7.5 7.5 0 3z"/><path d="M0 4.5l7.5 4.5 7.5-4.5V11H0z"/></svg>
          <span>colin@brightledgeplan.com.au</span>
        </li>
      </ul>
    </div>
  </section>

  <section class="card card--back" aria-label="Business card back">
    <div class="wordmark">BRIGHTLEDGE</div>
    <div class="company-info">
      <p>AFS Licence No. 518760</p>
      <p>www.brightledgeplan.com.au</p>
      <p>PO BOX 5307, PERTH BC, WA 6849</p>
    </div>
  </section>
</body>
</html>
```